Letterbox flyer design

Hi - hoping you're able to help design a flyer for letterbox delivery. I think it needs to be 99mm x 210mm.

Side 1 - Large Logo, dark back ground.
Larger text - "5%* Property Management."
Medium Text - "Better Services, Lower Fee's, Higher Yields"
Smaller text at bottom - "0472 519 084 - gideon@pellbrook.com.au - pellbrook.com.au"

Back Side -
• Management Fee – 5%+GST of rent collected (no rent paid = no mgmt. fee charged)
• An Establishment fee of $500 for new tenancies we establish.
• Marketing Costs as Required and agreed to between parties.
• No Fee’s for Condition Reports, inspections, re-listing, tenancy renewal, admin costs, or any other ‘sundry’ charges.
• All rent is paid out monthly, yearly ‘profit-and-loss’ statements at no cost.
• Ingoing condition report is produced prior to occupancy, and routine condition inspections are conducted after the first 3months, then every 6months.
• Open homes are advertised in advance, and held on the weekend and one lunchtime or evening per week.
• All applicants are vetted, with the most suitable sent through for your consideration and approval.
• Advise on different tenancy terms as they could have the ability to affect the long-term yields.

```html
<!DOCTYPE html>
<html lang="en">
<head>
<meta charset="utf-8">
<title>Pellbrook &amp; Co Property Services – Letterbox Flyer</title>
<link href="https://fonts.googleapis.com/css2?family=Oswald:wght@500;600;700&family=Lato:wght@700;900&display=swap" rel="stylesheet">
<style>
  :root{
    --page:#d9d9d9;
    --ink:#000000;
    --teal:#43bfc7;
    --grey:#8a8a8a;
    --grey-dark:#5d585c;
    --grey-light:#c7c6c7;
    --white:#ffffff;
  }
  *{margin:0;padding:0;box-sizing:border-box}
  html,body{width:1077px;height:1200px;overflow:hidden;background:var(--page)}
  body{position:relative;font-family:"Lato",Arial,sans-serif}

  .flyer{position:absolute;left:158px;width:761px;height:359px;background:var(--ink);overflow:hidden;box-shadow:0 1px 3px rgba(0,0,0,.25)}
  .flyer--front{top:200px}
  .flyer--back{top:641px}

  /* front */
  .brand{position:absolute;left:92px;top:31px;display:flex;align-items:center;gap:14px}
  .brand__mark{width:94px;height:94px;border:2px solid var(--teal);border-radius:50%}
  .brand__name{font-family:"Oswald",Arial,sans-serif;font-weight:500;color:var(--grey);line-height:1;text-transform:uppercase}
  .brand__name-main{display:block;font-size:44px;letter-spacing:-1px}
  .brand__name-sub{display:block;font-size:28px;letter-spacing:-.5px;margin-top:3px}

  .headline{position:absolute;left:45px;top:140px;display:flex;align-items:flex-start;font-family:"Oswald",Arial,sans-serif;font-weight:700;color:var(--teal);text-transform:uppercase;line-height:1}
  .headline__rate{font-size:118px;letter-spacing:-4px;line-height:.86;transform:scaleX(.9);transform-origin:left}
  .headline__star{font-size:48px;margin-left:-14px;line-height:.7}
  .headline__words{margin-left:4px;display:flex;flex-direction:column;gap:0}
  .headline__words span{font-size:56px;letter-spacing:-.5px;line-height:.84;transform:scaleX(.92);transform-origin:left}

  .tagline{position:absolute;left:42px;top:251px;width:445px;height:33px;border-radius:17px;background:var(--grey);display:flex;align-items:center;justify-content:center;font-family:"Oswald",Arial,sans-serif;font-weight:500;font-size:23px;color:var(--ink);text-transform:uppercase;letter-spacing:-.3px}

  .scene{position:absolute;left:529px;top:30px;width:232px;height:329px}
  .band-line{position:absolute;left:0;top:310px;width:540px;height:8px;background:var(--grey-light)}
  .contact-band{position:absolute;left:0;top:318px;width:761px;height:41px;background:var(--teal)}
  .contact{position:absolute;left:22px;top:330px;display:flex;align-items:center;gap:4px;font-weight:900;font-size:14px;color:var(--ink);letter-spacing:.1px;text-transform:uppercase}
  .contact__item{display:flex;align-items:center;gap:3px;margin-right:1px}
  .contact__item svg{width:12px;height:12px;fill:var(--ink)}

  /* back */
  .frame{position:absolute;left:15px;top:15px;width:731px;height:329px;border:2px solid var(--teal)}
  .terms{position:absolute;left:50px;top:50px;list-style:none;width:680px}
  .terms li{display:flex;gap:8px;font-weight:700;font-size:13.8px;line-height:17.5px;color:var(--white);margin-bottom:8.8px;letter-spacing:-.15px}
  .terms svg{flex:none;width:16px;height:16px;margin-top:1px}
</style>
</head>
<body>

<section class="flyer flyer--front" aria-label="Flyer front">
  <div class="brand">
    <div class="brand__mark"></div>
    <div class="brand__name">
      <span class="brand__name-main">Pellbrook &amp; Co</span>
      <span class="brand__name-sub">Property Services</span>
    </div>
  </div>

  <h1 class="headline">
    <span class="headline__rate">5%</span><span class="headline__star">*</span>
    <span class="headline__words"><span>Property</span><span>Management.</span></span>
  </h1>

  <p class="tagline">Better Services, Lower Fee's, Higher Yields</p>

  <svg class="scene" role="img" aria-label="Illustration of city buildings and houses" viewBox="0 0 232 329" preserveAspectRatio="none">
    <defs>
      <linearGradient id="sceneTone" x1="0" y1="0" x2="0" y2="1">
        <stop offset="0" stop-color="#5d585c"/>
        <stop offset=".7" stop-color="#3a3739"/>
        <stop offset="1" stop-color="#c7c6c7"/>
      </linearGradient>
    </defs>
    <rect width="232" height="329" fill="url(#sceneTone)"/>
  </svg>

  <div class="band-line"></div>
  <div class="contact-band"></div>
  <div class="contact">
    <span class="contact__item"><svg viewBox="0 0 24 24"><path d="M6.6 10.8a15.1 15.1 0 0 0 6.6 6.6l2.2-2.2a1 1 0 0 1 1-.25 11.4 11.4 0 0 0 3.6.57 1 1 0 0 1 1 1V20a1 1 0 0 1-1 1A17 17 0 0 1 3 4a1 1 0 0 1 1-1h3.5a1 1 0 0 1 1 1c0 1.25.2 2.45.57 3.57a1 1 0 0 1-.25 1z"/></svg>0472 519 084</span>
    <span class="contact__item"><svg viewBox="0 0 24 24"><path d="M2 5h20v14H2z M2 5l10 8 10-8" fill="none" stroke="#000" stroke-width="2.4"/></svg>gideon@pellbrook.com.au</span>
    <span class="contact__item"><svg viewBox="0 0 24 24"><circle cx="12" cy="12" r="9.5" fill="none" stroke="#000" stroke-width="2.4"/><path d="M2.5 12h19M12 2.5c3 3 3 16 0 19M12 2.5c-3 3-3 16 0 19" fill="none" stroke="#000" stroke-width="1.6"/></svg>pellbrook.com.au</span>
  </div>
</section>

<section class="flyer flyer--back" aria-label="Flyer back">
  <div class="frame"></div>
  <ul class="terms">
    <li><svg viewBox="0 0 16 16"><circle cx="8" cy="8" r="8" fill="#43bfc7"/><path d="M4.3 8.2l2.5 2.4 4.9-5" fill="none" stroke="#000" stroke-width="2"/></svg><span>Management Fee – 5%+GST of rent collected (no rent paid = no mgmt. fee charged)</span></li>
    <li><svg viewBox="0 0 16 16"><circle cx="8" cy="8" r="8" fill="#43bfc7"/><path d="M4.3 8.2l2.5 2.4 4.9-5" fill="none" stroke="#000" stroke-width="2"/></svg><span>An Establishment fee of $500 for new tenancies we establish.</span></li>
    <li><svg viewBox="0 0 16 16"><circle cx="8" cy="8" r="8" fill="#43bfc7"/><path d="M4.3 8.2l2.5 2.4 4.9-5" fill="none" stroke="#000" stroke-width="2"/></svg><span>Marketing Costs as Required and agreed to between parties.</span></li>
    <li><svg viewBox="0 0 16 16"><circle cx="8" cy="8" r="8" fill="#43bfc7"/><path d="M4.3 8.2l2.5 2.4 4.9-5" fill="none" stroke="#000" stroke-width="2"/></svg><span>No Fee’s for Condition Reports, inspections, re-listing, tenancy renewal, admin costs, or any other<br>‘sundry’ charges.</span></li>
    <li><svg viewBox="0 0 16 16"><circle cx="8" cy="8" r="8" fill="#43bfc7"/><path d="M4.3 8.2l2.5 2.4 4.9-5" fill="none" stroke="#000" stroke-width="2"/></svg><span>All rent is paid out monthly, yearly ‘profit-and-loss’ statements at no cost.</span></li>
    <li><svg viewBox="0 0 16 16"><circle cx="8" cy="8" r="8" fill="#43bfc7"/><path d="M4.3 8.2l2.5 2.4 4.9-5" fill="none" stroke="#000" stroke-width="2"/></svg><span>Ingoing condition report is produced prior to occupancy, and routine condition inspections<br>are conducted after the first 3months, then every 6months.</span></li>
    <li><svg viewBox="0 0 16 16"><circle cx="8" cy="8" r="8" fill="#43bfc7"/><path d="M4.3 8.2l2.5 2.4 4.9-5" fill="none" stroke="#000" stroke-width="2"/></svg><span>Open homes are advertised in advance, &amp; held on the weekend &amp; one lunchtime or evening per week.</span></li>
    <li><svg viewBox="0 0 16 16"><circle cx="8" cy="8" r="8" fill="#43bfc7"/><path d="M4.3 8.2l2.5 2.4 4.9-5" fill="none" stroke="#000" stroke-width="2"/></svg><span>All applicants are vetted, with the most suitable sent through for your consideration and approval.</span></li>
    <li><svg viewBox="0 0 16 16"><circle cx="8" cy="8" r="8" fill="#43bfc7"/><path d="M4.3 8.2l2.5 2.4 4.9-5" fill="none" stroke="#000" stroke-width="2"/></svg><span>Advise on different tenancy terms as they could have the ability to affect the long-term yields.</span></li>
  </ul>
</section>

</body>
</html>
```